Hot-air ballooning company needs a DL-size flyer

Skylark Aerial Tours is a hot-air ballooning company which flies passengers in the King Valley, Victoria, Australia.
We need a 2-sided DL-size flyer which promotes our hot-air balloon flights and packages.
Most of our customers are couples, and we want the flyer design to communicate safety, adventure, and romance.
The flyer should make the best use of our images which we provide, and we've also included a document with the text for the flyer.
Updates

2 days is not long enough to gather designs, the brief never asked me what my deadline should be.

Target Market(s)

Couples, buyers are majority female, between the ages of 20-60

Industry/Entity Type

Tourism

Font styles to use
Sans Serif

Colors

Designer to choose colors to be used in the design.

Requirements
Must have
• Communicate safety, adventure, and romance
• Use images
Nice to have
• There is a lot of text, it would be great if you could make it look like as little text as possible
Should not have
• No childish designs

```html
<!DOCTYPE html>
<html lang="en">
<head>
<meta charset="utf-8">
<title>Skylark Aerial Tours – Your Flight</title>
<link href="https://fonts.googleapis.com/css2?family=Open+Sans:wght@400;600;800&display=swap" rel="stylesheet">
<style>
  :root {
    --backdrop: #e6e6e8;
    --sun: #f8ea6e;
    --sun-soft: #fbf19a;
    --navy: #3b3d5a;
    --ink: #2f3150;
    --leaf: #8cc63f;
    --white: #ffffff;
  }
  * { margin: 0; padding: 0; box-sizing: border-box; }
  html, body { width: 1200px; height: 902px; overflow: hidden; }
  body {
    background: var(--backdrop);
    font-family: "Open Sans", Arial, sans-serif;
    position: relative;
  }
  .flyer {
    position: absolute;
    left: 397px; top: 21px;
    width: 406px; height: 860px;
    background: radial-gradient(circle at 40% 40%, var(--sun-soft), var(--sun) 70%);
    overflow: hidden;
    color: var(--ink);
    box-shadow: 0 6px 24px rgba(0,0,0,0.15);
  }
  .brand {
    position: absolute; left: 26px; top: 26px;
    display: flex; align-items: flex-start; gap: 8px;
  }
  .brand-dot {
    width: 18px; height: 18px; border-radius: 50%;
    background: var(--navy); margin-top: 2px;
  }
  .brand-name {
    font-weight: 800; font-size: 17px; line-height: 1.05;
    text-transform: uppercase; letter-spacing: 0.5px; color: var(--navy);
  }
  .brand-tag {
    font-size: 7px; letter-spacing: 1px; text-transform: uppercase;
    color: var(--navy); margin-top: 3px;
  }
  .photo-grid { position: absolute; left: 0; top: 0; }
  .flight-info {
    position: absolute; left: 34px; right: 28px; top: 318px;
  }
  .availability { font-size: 11px; text-align: center; }
  .section-title {
    font-weight: 800; font-size: 26px; text-align: center;
    letter-spacing: 1px; margin: 6px 0 12px;
  }
  .highlights { list-style: none; position: relative; }
  .highlights::before {
    content: ""; position: absolute; left: 3px; top: 8px; bottom: 8px;
    border-left: 1.5px dotted var(--ink);
  }
  .highlights li {
    position: relative; padding-left: 18px;
    font-size: 12.5px; line-height: 1.4; margin-bottom: 3px;
  }
  .highlights li::before {
    content: ""; position: absolute; left: 0; top: 6px;
    width: 7px; height: 7px; border-radius: 50%; background: var(--ink);
  }
  .footer-band { position: absolute; left: 0; bottom: 0; }
  .contact {
    position: absolute; right: 20px; bottom: 16px;
    text-align: right; color: var(--white);
    font-size: 10px; line-height: 1.45;
  }
</style>
</head>
<body>
  <main class="flyer">
    <svg class="photo-grid" width="406" height="330" viewBox="0 0 406 330">
      <defs>
        <linearGradient id="sky-balloon" x1="0" y1="0" x2="1" y2="1">
          <stop offset="0" stop-color="#6aa0d8"/><stop offset="1" stop-color="#e8c23a"/>
        </linearGradient>
        <linearGradient id="green-envelope" x1="0" y1="0" x2="1" y2="1">
          <stop offset="0" stop-color="#3f8f4a"/><stop offset="1" stop-color="#2c5f9e"/>
        </linearGradient>
        <linearGradient id="flame-glow" x1="0" y1="0" x2="1" y2="1">
          <stop offset="0" stop-color="#e8452c"/><stop offset="1" stop-color="#f4a42a"/>
        </linearGradient>
        <linearGradient id="valley-view" x1="0" y1="0" x2="1" y2="1">
          <stop offset="0" stop-color="#8fb4d6"/><stop offset="1" stop-color="#5a6a4c"/>
        </linearGradient>
      </defs>
      <g transform="translate(300 170) rotate(45)">
        <rect x="-104" y="-104" width="208" height="208" fill="var(--navy)"/>
        <rect x="-98" y="-98" width="95" height="95" fill="url(#sky-balloon)" role="img" aria-label="Striped hot-air balloon rising over the valley"/>
        <rect x="3" y="-98" width="95" height="95" fill="url(#green-envelope)" role="img" aria-label="Looking up into a green and blue balloon envelope"/>
        <rect x="-98" y="3" width="95" height="95" fill="url(#flame-glow)" role="img" aria-label="Burner flame inflating an orange balloon at dawn"/>
        <rect x="3" y="3" width="95" height="95" fill="url(#valley-view)" role="img" aria-label="Balloons drifting above King Valley hills"/>
      </g>
    </svg>

    <header class="brand">
      <span class="brand-dot"></span>
      <div>
        <div class="brand-name">Skylark<br>Aerial Tours</div>
        <div class="brand-tag">King Valley hot air ballooning</div>
      </div>
    </header>

    <section class="flight-info">
      <p class="availability">Mansfield flights are also available</p>
      <h1 class="section-title">YOUR FLIGHT</h1>
      <ul class="highlights">
        <li>One-hour sunrise balloon flight in the spectacular King Valley region in North East Victoria</li>
        <li>Delicious champagne breakfast after the flight (recommended option)</li>
        <li>Informative details throughout your experience with our expert crew</li>
        <li>The opportunity to be involved in the inflation and deflation process should you wish</li>
        <li>Safe, friendly and professional</li>
        <li>The flight lasts approximately 1 hour</li>
        <li>The entire experience takes about 3-4 hours</li>
        <li>Suitable from age 7 to 97</li>
        <li>Gift Certificates are also available</li>
      </ul>
    </section>

    <svg class="footer-band" width="406" height="190" viewBox="0 0 406 190">
      <polygon points="0,0 0,30 40,30" fill="var(--leaf)"/>
      <polygon points="0,30 406,100 406,190 0,190" fill="var(--navy)"/>
    </svg>

    <footer class="contact">
      For bookings or more information:<br>
      www.skylarkaerialtours.com.au<br>
      flights@skylarkaerialtours.com.au<br>
      Skylark Aerial Tours operates under Air Operator's Certificate<br>
      AOC 5512-14 issued by the National Air Safety Office
    </footer>
  </main>
</body>
</html>
```